Substance abuse awareness flyer for school age kids

I am needing a flyer for school-age kids. What if it were designed to look like an Travlo with someone texting and the text bubbles were some of the text below with emojis? Maybe a text chain between to friends:

Maybe the first text bubble says "I'm thinking about using drugs and alcohol"
the next bubble: "Just say no!" ( perhaps a stop sign emoji ?)

"Talk to your parents, your teachers at school, or your doctor about how drugs and alcohol can harm you"

another text bubble "did you know that alcohol and drugs could lead to..."
then include some of the info below (see links for more info).
Where ever you get info, it must be cited.

this needs to be English on one side and Spanish on the other side and needs to include the logo attached.

The effects of substance abuse
BWR: https://www.bwr-example.org/kvtmpl/yrnq/articles/youth-risk-habits.html
Affect growth and development, especially brain development. Not able to focus at school or be around friends. https://www.healthyminds-sample.org/pages/shared/docs/stayingclear_2.pdf
Leads to risky behaviors and lack of impulse control (dangerous activities) https://www.healthyminds-sample.org/pages/shared/docs/stayingclear_2.pdf
Contribute to health problems as an adult: heart disease, high blood pressure, and trouble sleeping.

Target Market(s)

school age kids 9-20

Requirements
Must have
• Print ready: 8.5x11

```html
<!DOCTYPE html>
<html lang="en">
<head>
<meta charset="utf-8">
<title>Say No to Drugs and Alcohol – Flyer</title>
<link href="https://fonts.googleapis.com/css2?family=Montserrat:wght@500;600;700;800&display=swap" rel="stylesheet">
<style>
  :root {
    --sky: #1077c0;
    --aqua: #72cbe0;
    --lime: #bfd630;
    --maroon: #5e2535;
    --ink: #1a1a1a;
    --white: #ffffff;
    --violet-a: #6a3fa6;
    --violet-b: #b9a6dc;
  }
  * { margin: 0; padding: 0; box-sizing: border-box; }
  html, body { width: 1029px; height: 1200px; overflow: hidden; background: var(--white); }
  body { font-family: 'Montserrat', sans-serif; color: var(--ink); }
  .flyer { position: relative; width: 1029px; height: 1200px; overflow: hidden; background: var(--white); }
  .backdrop { position: absolute; inset: 0; }
  .bubble-text { position: absolute; font-weight: 700; }
  .bubble-question { left: 149px; top: 56px; width: 350px; font-size: 19px; line-height: 22px; text-transform: uppercase; letter-spacing: 0.2px; }
  .bubble-refuse { left: 511px; top: 160px; width: 246px; text-align: center; font-size: 25px; font-weight: 800; }
  .bubble-advice { left: 421px; top: 246px; width: 380px; font-size: 18.5px; line-height: 22.5px; font-weight: 600; }
  .bubble-facts { left: 304px; top: 410px; width: 438px; font-size: 20.5px; line-height: 24.5px; }
  .bubble-source { display: block; text-align: right; color: var(--white); font-size: 19px; line-height: 22px; }
  .brand { position: absolute; right: 14px; top: 22px; width: 130px; display: flex; align-items: center; gap: 7px; }
  .brand-dot { flex: none; width: 16px; height: 16px; border-radius: 50%; background: var(--sky); }
  .brand-name { font-size: 13px; line-height: 15px; font-weight: 700; color: var(--maroon); }
  .risks-heading { position: absolute; left: 0; top: 702px; width: 408px; height: 42px; background: var(--sky); color: var(--white); border-radius: 0 24px 24px 0; font-size: 25px; font-weight: 800; line-height: 42px; padding-left: 12px; }
  .risks-list { position: absolute; left: 12px; top: 758px; width: 720px; list-style: none; }
  .risks-list li { position: relative; padding-left: 14px; font-size: 18.5px; line-height: 22px; font-weight: 500; margin-bottom: 26px; }
  .risks-list li::before { content: ""; position: absolute; left: 1px; top: 9px; width: 6px; height: 6px; border-radius: 50%; background: var(--sky); }
  .summary-band { position: absolute; left: 0; top: 940px; width: 1029px; height: 164px; background: var(--aqua); padding: 10px 12px 0 12px; font-size: 24.5px; line-height: 29px; font-weight: 800; letter-spacing: -0.1px; }
  .cta { position: absolute; left: 234px; top: 1131px; width: 557px; height: 59px; border-radius: 30px; background: var(--sky); color: var(--white); font-size: 29px; font-weight: 800; text-align: center; line-height: 59px; }
</style>
</head>
<body>
<main class="flyer">
  <svg class="backdrop" width="1029" height="1200" viewBox="0 0 1029 1200" aria-hidden="false">
    <defs>
      <clipPath id="sky-area">
        <path d="M0,0 H894 Q960,60 1029,121 V849 C800,840 620,800 480,720 C380,660 250,600 0,611 Z"/>
      </clipPath>
      <linearGradient id="friend-tone" x1="0" y1="0" x2="1" y2="1">
        <stop offset="0" stop-color="var(--violet-a)"/>
        <stop offset="1" stop-color="var(--violet-b)"/>
      </linearGradient>
    </defs>
    <path class="sky" d="M0,0 H894 Q960,60 1029,121 V849 C800,840 620,800 480,720 C380,660 250,600 0,611 Z" fill="var(--sky)"/>
    <g clip-path="url(#sky-area)">
      <rect role="img" aria-label="Illustration of a teen seen from behind, holding a phone and texting" x="0" y="155" width="276" height="470" rx="30" fill="url(#friend-tone)"/>
      <rect role="img" aria-label="Illustration of a second teen seen from behind, reading a message on a phone" x="756" y="324" width="300" height="540" rx="30" fill="url(#friend-tone)"/>
    </g>
    <path class="wave-line" d="M0,611 C250,600 380,660 480,720 C620,800 800,840 1029,849" fill="none" stroke="var(--maroon)" stroke-width="8"/>
    <path class="bubble question" d="M131,40 H507 V125 H280 L194,149 L232,125 H131 Z" fill="var(--lime)"/>
    <path class="bubble refuse" d="M511,151 H757 V203 H734 L716,219 L670,203 H511 Z" fill="var(--aqua)"/>
    <path class="bubble advice" d="M392,233 H806 V344 H710 L737,378 L640,344 H392 Z" fill="var(--aqua)"/>
    <path class="bubble facts" d="M283,395 H746 V582 H658 L668,640 L564,582 H283 Z" fill="var(--aqua)"/>
  </svg>

  <div class="brand"><span class="brand-dot"></span><span class="brand-name">Riverbend Care Network</span></div>

  <p class="bubble-text bubble-question">I'm thinking about using drugs and alcohol</p>
  <p class="bubble-text bubble-refuse">JUST SAY NO!</p>
  <p class="bubble-text bubble-advice">Talk to your parents, your teachers at school, or your doctor about how drugs and alcohol can harm you.</p>
  <p class="bubble-text bubble-facts">Did you know that alcohol and drugs could lead to - The development of chronic diseases and other serious problems including: High blood pressure, heart disease, stroke, liver disease, and digestive problems.<span class="bubble-source">-bwr-example.org</span></p>

  <h2 class="risks-heading">RISKS OF SUBSTANCE USE</h2>
  <ul class="risks-list">
    <li>Affect the growth and development of teens,<br>especially brain development.</li>
    <li>Occur more frequently with other risky behaviors.</li>
    <li>If you use drugs and alcohol at an early age,<br>it increases your chances of becoming addicted later in life</li>
  </ul>

  <p class="summary-band">Finally, the earlier teens start using substances, the greater their chances of continuing to use substances and developing substance use problems later in life. When teens begin drinking at an early age, they increase the chance of becoming addicted to or continuing to abuse substances later in life.</p>

  <p class="cta">Say No to Drugs and Alcohol!</p>
</main>
</body>
</html>
```